Social Media Graphics - ALL TEXT KB

We are looking for a series of social media graphics for Instagram (standard size 1:1 (1080x1080px) that are ALL TEXT. We want the following quotes below on each graphic; one quote per graphic. AND, In very small letters at the bottom of each graphic, add @KBWardleOnline

The look and feel of these graphics should be complimentary to the color palette attached below; but keep them simple. But the design is up to you; at the end of this document, I provided various samples of all text graphics that I like as examples.

Target Market(s)

women looking to lose weight

Industry/Entity Type

health and wellness

Colors
E54698
E96AAD
F1A4CE
F9D9EA
FCEFF6

Requirements
Must have
• the quotes in the document
Should not have
• no stock photography

```html
<!DOCTYPE html>
<html lang="en">
<head>
<meta charset="utf-8">
<title>Flatter Belly Quote</title>
<link href="https://fonts.googleapis.com/css2?family=Montserrat:wght@800&family=Roboto+Condensed:wght@300&display=swap" rel="stylesheet">
<style>
:root{
  --magenta:#df1478;
  --pink-mid:#e96aad;
  --pink-soft:#f1a4ce;
  --pink-pale:#fceff6;
  --white:#ffffff;
}
*{margin:0;padding:0;box-sizing:border-box}
html,body{width:1200px;height:1200px;overflow:hidden}
.post{
  position:relative;width:1200px;height:1200px;
  background:
    radial-gradient(circle at 100% 4%, var(--pink-pale) 0%, var(--pink-soft) 22%, var(--pink-mid) 42%, rgba(223,20,120,0) 68%),
    var(--magenta);
}
.post-frame{position:absolute;left:0;top:0}
.quote{
  position:absolute;left:165px;top:152px;
  font-family:'Montserrat',sans-serif;font-weight:800;
  color:var(--white);font-size:78px;line-height:136px;
  letter-spacing:0.5px;text-transform:uppercase;
}
.quote span{display:block;white-space:nowrap}
.quote .indent{padding-left:23px}
.handle{
  position:absolute;left:178px;top:980px;
  font-family:'Roboto Condensed',sans-serif;font-weight:300;
  color:var(--white);font-size:36px;line-height:1;white-space:nowrap;
}
</style>
</head>
<body>
<div class="post">
  <svg class="post-frame" width="1200" height="1200" viewBox="0 0 1200 1200">
    <defs>
      <linearGradient id="frame-top" x1="0" y1="0" x2="1" y2="0">
        <stop offset="0" stop-color="#ffffff"/>
        <stop offset="0.4" stop-color="#df1478"/>
        <stop offset="1" stop-color="#df1478"/>
      </linearGradient>
      <linearGradient id="frame-right" x1="0" y1="0" x2="0" y2="1">
        <stop offset="0" stop-color="#df1478"/>
        <stop offset="0.55" stop-color="#df1478"/>
        <stop offset="0.85" stop-color="#ffffff"/>
        <stop offset="1" stop-color="#ffffff"/>
      </linearGradient>
    </defs>
    <rect x="46" y="61" width="1108" height="12" fill="url(#frame-top)"/>
    <rect x="1142" y="61" width="12" height="1078" fill="url(#frame-right)"/>
    <rect x="46" y="61" width="12" height="1078" fill="#ffffff"/>
    <rect x="46" y="1127" width="1108" height="12" fill="#ffffff"/>
  </svg>
  <p class="quote">
    <span>Wake up</span>
    <span>tomorrow with a</span>
    <span class="indent">flatter belly- yes,</span>
    <span class="indent">this overnight</span>
    <span class="indent">remedy works</span>
    <span class="indent">like magic!</span>
  </p>
  <p class="handle">@KBWardleOnline</p>
</div>
</body>
</html>
```